Best Seller Cover Design for Inspirational Non-Fiction, Self-Help Book

I've been working diligently on a book title "Quiet Harbor Rising" that will be pivotal for my coaching business. We're heavily investing in marketing and public relations for this and would love it to be a best seller (every other's dream). I need an amazing book cover design that is eye-catching, description, creative, interesting, and compelling, Can you work your magic?I've attached a detailed description along with the content for the back cover. Please let me know if all the content does not fit and I'm happy to reduce it. I need a cover that sells and speaks to the description, whatever you think that will be best. Book DetailsTitle: Self-Defined SuccessSubtitle: Spoiler Alert: You Already Have Everything It TakesAuthor: Ngan H. NguyenSpecifics:- The book will be 5.5" by 8.5" and 216 pages (may change slightly and we can update the spine in final revisions). - Paperback and leave space for a bar code- Will need the raw files so this can be redesigned into hardcover down the line- Brindlemark book cover upload ready- Final file will also need the front cover only for e-book version- Add profile headshot (attached) to back-cover if space permits.I do not have a clear vision of what will be best for this cover but I really like the evocative style of Walter Okonjo Overflowing book. Thank you!

Target Market(s)

Professionals in transition, aspiring or new entrepreneurs, change-makers.

Font styles to use
Serif
Script

Colors

Designer to choose colors to be used in the design.

Requirements
Must have
• Traditional but with elements that make it interesting and provocative since it is speaking to a twist on a topic that has been well talked about, success.

```html
<!DOCTYPE html>
<html lang="en">
<head>
<meta charset="utf-8">
<title>Quiet Harbor Rising — Book Cover</title>
<link href="https://fonts.googleapis.com/css2?family=Anton&display=swap" rel="stylesheet">
<style>
  :root {
    --canvas-bg: #cfe0e2;
    --cover-stone-light: #b9b7a6;
    --cover-stone-mid: #9c9c8e;
    --cover-stone-dark: #7f8279;
    --tape-yellow: #e6c21c;
    --tape-yellow-shade: #c9a614;
    --tape-ink: #141210;
  }
  html, body {
    margin: 0;
    padding: 0;
    width: 1200px;
    height: 1000px;
    overflow: hidden;
    background: var(--canvas-bg);
  }
  .stage {
    position: relative;
    width: 1200px;
    height: 1000px;
  }
  .book-cover {
    position: absolute;
    left: 322px;
    top: 70px;
    width: 556px;
    height: 860px;
  }
  .tape-label {
    font-family: "Anton", "Oswald", sans-serif;
    fill: var(--tape-ink);
    letter-spacing: 0.5px;
  }
</style>
</head>
<body>
<main class="stage">
  <svg class="book-cover" viewBox="0 0 556 860" aria-labelledby="cover-title">
    <title id="cover-title">Quiet Harbor Rising</title>
    <defs>
      <clipPath id="cover-edge">
        <rect width="556" height="860"/>
      </clipPath>
      <radialGradient id="stone-tone" cx="45%" cy="40%" r="75%">
        <stop offset="0%" stop-color="var(--cover-stone-light)"/>
        <stop offset="55%" stop-color="var(--cover-stone-mid)"/>
        <stop offset="100%" stop-color="var(--cover-stone-dark)"/>
      </radialGradient>
    </defs>

    <g clip-path="url(#cover-edge)">
      <rect class="cover-texture" width="556" height="860" fill="url(#stone-tone)"
            role="img" aria-label="Weathered grey concrete texture filling the cover"/>

      <!-- back tape, gentle downward slant -->
      <g class="caution-tape" transform="translate(330 205) rotate(-9)">
        <rect x="-450" y="-26" width="900" height="52" fill="var(--tape-yellow)"/>
        <text class="tape-label" x="40" y="18" font-size="42" text-anchor="middle">QUIET HARBOR RISING</text>
      </g>

      <!-- near-level tape behind the big cross -->
      <g class="caution-tape" transform="translate(300 435) rotate(3)">
        <rect x="-450" y="-23" width="900" height="46" fill="var(--tape-yellow-shade)"/>
        <text class="tape-label" x="-40" y="16" font-size="38" text-anchor="middle">QUIET HARBOR RISING</text>
      </g>

      <!-- long tape running down to the right -->
      <g class="caution-tape" transform="translate(290 400) rotate(22)">
        <rect x="-480" y="-32" width="960" height="64" fill="var(--tape-yellow)"/>
        <text class="tape-label" x="-30" y="22" font-size="54" text-anchor="middle">QUIET HARBOR RISING</text>
      </g>

      <!-- front tape rising to the right -->
      <g class="caution-tape" transform="translate(285 455) rotate(-22)">
        <rect x="-480" y="-40" width="960" height="80" fill="var(--tape-yellow)"/>
        <text class="tape-label" x="10" y="27" font-size="68" text-anchor="middle">QUIET HARBOR RISING</text>
      </g>
    </g>
  </svg>
</main>
</body>
</html>
```